Minimalist Planner/Journal Design

We need a planner/journal designed for daily use in a small group. I've attached a requirements document that outlines what every page needs to have on it. I've also attached a basic rough draft that we had made in Canva but the draft needs to be redesigned to look more in line with the style we need. I've attached some sample pages from some planners we like the style of. Feel free to add your own creativity and stylistic choices but keep in mind we are trying to get a very 'clean and minimalist design'. The deliverables should be both a pdf of the 8 planner pages, as well as the photoshop/gimp/illustrator files for the project.

Font styles to use
Other font styles liked:
• You choose, but we prefer thin , basic/minimal font faces

Requirements
Must have
• Minimal Design

```html
<!DOCTYPE html>
<html lang="en">
<head>
<meta charset="utf-8">
<title>Minimalist Planner – Page Spreads</title>
<link href="https://fonts.googleapis.com/css2?family=Montserrat:wght@300;400&display=swap" rel="stylesheet">
<style>
  :root {
    --backdrop: #808080;
    --paper: #ffffff;
    --ink: #1a1a1a;
    --muted: #6e6e6e;
    --day-fill: #f3f3f3;
    --label: #ffffff;
  }
  * { margin: 0; padding: 0; box-sizing: border-box; }
  html, body {
    width: 927px;
    height: 1200px;
    overflow: hidden;
    background: var(--backdrop);
    font-family: "Montserrat", sans-serif;
  }
  .sheet-board { position: relative; width: 927px; height: 1200px; }
  .page-label {
    position: absolute;
    color: var(--label);
    font-size: 12.5px;
    font-weight: 300;
    letter-spacing: 0.02em;
  }
  .page {
    position: absolute;
    width: 392px;
    height: 507px;
    background: var(--paper);
    box-shadow: 0 2px 8px rgba(0,0,0,0.45);
  }
  .page svg { display: block; width: 100%; height: 100%; }
  .page text {
    font-family: "Montserrat", sans-serif;
    font-size: 12.5px;
    font-weight: 400;
    fill: var(--ink);
  }
  .page text.day-name { fill: var(--muted); font-size: 11.5px; }
  .page text.spaced { letter-spacing: 0.25em; }
  .rule { stroke: var(--ink); stroke-width: 1; }
  .rule-dot { stroke: var(--ink); stroke-width: 0.8; stroke-dasharray: 1 1.5; }
  .box { fill: none; stroke: var(--ink); stroke-width: 1.2; }
  .day-cell { fill: var(--day-fill); }
  .dot { fill: var(--ink); }
</style>
</head>
<body>
<main class="sheet-board">

  <span class="page-label" style="left:50px; top:42px;">PAGE 1</span>
  <span class="page-label" style="left:472px; top:42px;">PAGE 2</span>
  <span class="page-label" style="left:49px; top:1134px;">PAGE 3</span>
  <span class="page-label" style="left:472px; top:1134px;">PAGE 4</span>

  <!-- Daily page -->
  <section class="page daily-page" style="left:50.5px; top:75px;">
    <svg viewBox="0 0 714 923" aria-label="Daily planner page">
      <text x="43" y="53" class="spaced">WEEK:</text>
      <g class="box">
        <circle cx="120" cy="49" r="7.5"/><circle cx="143.5" cy="49" r="7.5"/>
        <circle cx="167" cy="49" r="7.5"/><circle cx="190.5" cy="49" r="7.5"/>
        <circle cx="214" cy="49" r="7.5"/><circle cx="237.5" cy="49" r="7.5"/>
        <circle cx="261" cy="49" r="7.5"/><circle cx="284.5" cy="49" r="7.5"/>
      </g>
      <text x="576" y="52">/</text><text x="609" y="52">/</text>

      <text x="43" y="105">PRIMARY TASKS</text>
      <g class="primary-task">
        <rect class="box" x="43.5" y="126.5" width="15" height="15"/>
        <text x="72" y="138">1.</text>
        <line class="rule" x1="71" y1="141.5" x2="335" y2="141.5"/>
        <line class="rule-dot" x1="71" y1="163.5" x2="335" y2="163.5"/>
        <line class="rule-dot" x1="71" y1="186.5" x2="335" y2="186.5"/>
      </g>
      <g class="primary-task" transform="translate(0,84)">
        <rect class="box" x="43.5" y="126.5" width="15" height="15"/>
        <text x="72" y="138">2.</text>
        <line class="rule" x1="71" y1="141.5" x2="335" y2="141.5"/>
        <line class="rule-dot" x1="71" y1="163.5" x2="335" y2="163.5"/>
        <line class="rule-dot" x1="71" y1="186.5" x2="335" y2="186.5"/>
      </g>
      <g class="primary-task" transform="translate(0,168)">
        <rect class="box" x="43.5" y="126.5" width="15" height="15"/>
        <text x="72" y="138">3.</text>
        <line class="rule" x1="71" y1="141.5" x2="335" y2="141.5"/>
        <line class="rule-dot" x1="71" y1="163.5" x2="335" y2="163.5"/>
        <line class="rule-dot" x1="71" y1="186.5" x2="335" y2="186.5"/>
      </g>

      <text x="44" y="416">SECONDARY TASKS</text>
      <g class="secondary-lines rule">
        <line x1="44" y1="445.5" x2="335" y2="445.5"/><line x1="44" y1="469" x2="335" y2="469"/>
        <line x1="44" y1="492.5" x2="335" y2="492.5"/><line x1="44" y1="516" x2="335" y2="516"/>
        <line x1="44" y1="539.5" x2="335" y2="539.5"/><line x1="44" y1="563" x2="335" y2="563"/>
        <line x1="44" y1="586.5" x2="335" y2="586.5"/><line x1="44" y1="610" x2="335" y2="610"/>
        <line x1="44" y1="633.5" x2="335" y2="633.5"/><line x1="44" y1="657" x2="335" y2="657"/>
        <line x1="44" y1="680.5" x2="335" y2="680.5"/><line x1="44" y1="704" x2="335" y2="704"/>
        <line x1="44" y1="727.5" x2="335" y2="727.5"/><line x1="44" y1="751" x2="335" y2="751"/>
        <line x1="44" y1="774.5" x2="335" y2="774.5"/>
      </g>

      <g class="schedule">
        <line class="rule" x1="467.5" y1="142" x2="467.5" y2="774"/>
        <g class="rule">
          <line x1="385" y1="142" x2="671" y2="142"/><line x1="385" y1="173.5" x2="671" y2="173.5"/>
          <line x1="385" y1="205.5" x2="671" y2="205.5"/><line x1="385" y1="237" x2="671" y2="237"/>
          <line x1="385" y1="269" x2="671" y2="269"/><line x1="385" y1="300.5" x2="671" y2="300.5"/>
          <line x1="385" y1="332.5" x2="671" y2="332.5"/><line x1="385" y1="364" x2="671" y2="364"/>
          <line x1="385" y1="396" x2="671" y2="396"/><line x1="385" y1="427.5" x2="671" y2="427.5"/>
          <line x1="385" y1="459.5" x2="671" y2="459.5"/><line x1="385" y1="491" x2="671" y2="491"/>
          <line x1="385" y1="523" x2="671" y2="523"/><line x1="385" y1="554.5" x2="671" y2="554.5"/>
          <line x1="385" y1="586.5" x2="671" y2="586.5"/><line x1="385" y1="618" x2="671" y2="618"/>
          <line x1="385" y1="650" x2="671" y2="650"/><line x1="385" y1="681.5" x2="671" y2="681.5"/>
          <line x1="385" y1="713.5" x2="671" y2="713.5"/><line x1="385" y1="745" x2="671" y2="745"/>
          <line x1="385" y1="774.5" x2="671" y2="774.5"/>
        </g>
        <g text-anchor="middle">
          <text x="423" y="159">5 AM</text><text x="423" y="191">6 AM</text>
          <text x="423" y="222">7 AM</text><text x="423" y="254">8 AM</text>
          <text x="423" y="286">9 AM</text><text x="420" y="318">10 AM</text>
          <text x="421" y="349">11 AM</text><text x="421" y="381">12 PM</text>
          <text x="424" y="413">1 PM</text><text x="424" y="445">2 PM</text>
          <text x="424" y="476">3 PM</text><text x="424" y="508">5 PM</text>
          <text x="424" y="540">6 PM</text><text x="424" y="572">7 PM</text>
          <text x="424" y="603">8 PM</text><text x="424" y="635">9 PM</text>
          <text x="421" y="667">10 PM</text><text x="421" y="699">10 PM</text>
          <text x="421" y="730">10 PM</text><text x="421" y="762">10 PM</text>
        </g>
      </g>

      <g class="daily-checks">
        <rect class="box" x="44.5" y="814.5" width="14" height="14"/>
        <text x="73" y="826">PHYSICAL ACTIVITY</text>
        <rect class="box" x="44.5" y="840" width="14" height="14"/>
        <text x="73" y="851.5">HABIT</text>
        <rect class="box" x="44.5" y="865.5" width="14" height="14"/>
        <text x="73" y="877">WEEKLY CHALLENGE</text>
      </g>
      <text x="643" y="881" text-anchor="end">DAILY SCORE W/L</text>
      <rect class="box" x="653.5" y="862.5" width="17" height="17" stroke-width="1.5"/>
      <path d="M657.5 871 L661 875.5 L667 865.5" fill="none" stroke="var(--ink)" stroke-width="1.8"/>
    </svg>
  </section>

  <!-- Notes page -->
  <section class="page notes-page" style="left:475px; top:75px;">
    <svg viewBox="0 0 714 923" aria-label="Dot-grid notes page">
      <defs>
        <pattern id="dot-grid-full" x="43" y="98.5" width="22.78" height="23.6" patternUnits="userSpaceOnUse">
          <circle class="dot" cx="1.5" cy="1.5" r="1"/>
        </pattern>
      </defs>
      <text x="44" y="52">NOTE</text>
      <line class="rule" x1="44" y1="65.5" x2="672" y2="65.5"/>
      <rect x="43" y="98.5" width="620" height="784" fill="url(#dot-grid-full)"/>
    </svg>
  </section>

  <!-- Weekly planning page -->
  <section class="page weekly-planning-page" style="left:50.5px; top:615.5px;">
    <svg viewBox="0 0 714 923" aria-label="Weekly planning page">
      <text x="43" y="53">WEEKLY PLANNING</text>
      <g class="box">
        <circle cx="194" cy="49" r="7.5"/><circle cx="217.7" cy="49" r="7.5"/>
        <circle cx="241.5" cy="49" r="7.5"/><circle cx="265.2" cy="49" r="7.5"/>
        <circle cx="289" cy="49" r="7.5"/><circle cx="312.7" cy="49" r="7.5"/>
        <circle cx="336.5" cy="49" r="7.5"/><circle cx="360.2" cy="49" r="7.5"/>
        <circle cx="384" cy="49" r="7.5"/><circle cx="407.7" cy="49" r="7.5"/>
        <circle cx="431.5" cy="49" r="7.5"/><circle cx="455.2" cy="49" r="7.5"/>
        <circle cx="479" cy="49" r="7.5"/>
      </g>
      <text x="576" y="52">/</text><text x="609" y="52">/</text>

      <text x="43" y="111">WEEKLY CHALLENGE</text>
      <rect class="box" x="43.5" y="126.5" width="627" height="75.5"/>
      <line class="rule" x1="586.5" y1="126.5" x2="586.5" y2="202"/>
      <text x="59" y="153">LOREM IPSUM DOLOR SIT AMET, CONSECTETUR ADIPISCING ELIT, SED DO</text>
      <text x="59" y="170">EIUSMOD TEMPOR INCIDIDUNT UT LABORE ET DOLORE MAGNA ALIQUA.</text>
      <text x="59" y="187">UT ENIM AD MINIM VENIAM, QUIS NOSTRUD EXERCITATION ULLAMC</text>

      <text x="43" y="254">3 WEELKY GOALS</text>
      <g class="weekly-goal">
        <rect class="box" x="43.5" y="285.5" width="15" height="15"/>
        <text x="72" y="297">1.</text>
        <line class="rule" x1="71" y1="301.5" x2="671" y2="301.5"/>
        <line class="rule-dot" x1="71" y1="322.5" x2="671" y2="322.5"/>
        <line class="rule-dot" x1="71" y1="346.5" x2="671" y2="346.5"/>
      </g>
      <g class="weekly-goal" transform="translate(0,84)">
        <rect class="box" x="43.5" y="285.5" width="15" height="15"/>
        <text x="72" y="297">2.</text>
        <line class="rule" x1="71" y1="301.5" x2="671" y2="301.5"/>
        <line class="rule-dot" x1="71" y1="322.5" x2="671" y2="322.5"/>
        <line class="rule-dot" x1="71" y1="346.5" x2="671" y2="346.5"/>
      </g>
      <g class="weekly-goal" transform="translate(0,168)">
        <rect class="box" x="43.5" y="285.5" width="15" height="15"/>
        <text x="72" y="297">3.</text>
        <line class="rule" x1="71" y1="301.5" x2="671" y2="301.5"/>
        <line class="rule-dot" x1="71" y1="322.5" x2="671" y2="322.5"/>
        <line class="rule-dot" x1="71" y1="352.5" x2="671" y2="352.5"/>
      </g>

      <g class="week-grid">
        <rect class="day-cell" x="43" y="564" width="315" height="102"/>
        <rect class="day-cell" x="362" y="564" width="309" height="102"/>
        <rect class="day-cell" x="43" y="671" width="315" height="102"/>
        <rect class="day-cell" x="362" y="671" width="309" height="102"/>
        <rect class="day-cell" x="43" y="778" width="315" height="102"/>
        <rect class="day-cell" x="362" y="778" width="309" height="102"/>
        <text class="day-name" x="56" y="584">MONDAY</text>
        <text class="day-name" x="375" y="584">TUESDAY</text>
        <text class="day-name" x="57" y="694">WEDNESDAY</text>
        <text class="day-name" x="375" y="694">THURSDAY</text>
        <text class="day-name" x="56" y="799">FRIDAY</text>
        <text class="day-name" x="375" y="799">SATURDAY &amp; SUNDAY</text>
      </g>
    </svg>
  </section>

  <!-- Weekly review page -->
  <section class="page weekly-review-page" style="left:475px; top:615.5px;">
    <svg viewBox="0 0 714 923" aria-label="Weekly review page">
      <defs>
        <pattern id="dot-grid-review" x="43" y="550.5" width="22.78" height="23.6" patternUnits="userSpaceOnUse">
          <circle class="dot" cx="1.5" cy="1.5" r="1"/>
        </pattern>
      </defs>
      <text x="43" y="53">WEEKLY REVIEW</text>
      <text x="577" y="52">/</text><text x="610" y="52">/</text>

      <g class="review-question">
        <text x="43" y="90">WHAT DID I LEARN THIS WEEK/ WHAT CAN I TAKE AWAY?</text>
        <line class="rule" x1="43" y1="99.5" x2="671" y2="99.5"/>
        <line class="rule-dot" x1="43" y1="122.5" x2="671" y2="122.5"/>
        <line class="rule-dot" x1="43" y1="145.5" x2="671" y2="145.5"/>
        <line class="rule-dot" x1="43" y1="169.5" x2="671" y2="169.5"/>
        <line class="rule-dot" x1="43" y1="192.5" x2="671" y2="192.5"/>
      </g>
      <g class="review-question">
        <text x="43" y="232">DID I EXECUTE WHAT I NEEDED TO MOVE FORWARD IN MY GOALS?</text>
        <line class="rule" x1="43" y1="246.5" x2="671" y2="246.5"/>
        <line class="rule-dot" x1="43" y1="268.5" x2="671" y2="268.5"/>
        <line class="rule-dot" x1="43" y1="292.5" x2="671" y2="292.5"/>
        <line class="rule-dot" x1="43" y1="315.5" x2="671" y2="315.5"/>
        <line class="rule-dot" x1="43" y1="338.5" x2="671" y2="338.5"/>
      </g>
      <g class="review-question">
        <text x="43" y="380">WHAT CAN I IMPROVE/KEEP DOING FOR NEXT WEEK?</text>
        <line class="rule" x1="43" y1="393.5" x2="671" y2="393.5"/>
        <line class="rule-dot" x1="43" y1="416.5" x2="671" y2="416.5"/>
        <line class="rule-dot" x1="43" y1="439.5" x2="671" y2="439.5"/>
        <line class="rule-dot" x1="43" y1="463.5" x2="671" y2="463.5"/>
        <line class="rule-dot" x1="43" y1="486.5" x2="671" y2="486.5"/>
      </g>

      <text x="43" y="524">NOTE</text>
      <line class="rule" x1="43" y1="532.5" x2="671" y2="532.5"/>
      <rect x="43" y="550.5" width="620" height="255" fill="url(#dot-grid-review)"/>

      <text x="43" y="848">DAILY SCORE W/L</text>
      <text x="311" y="848">DAILY SCORE W/L</text>
      <g class="score-row">
        <rect class="box" x="43.5" y="856.5" width="388" height="24" stroke-width="1"/>
        <g class="rule">
          <line x1="78.8" y1="856.5" x2="78.8" y2="880.5"/><line x1="114.1" y1="856.5" x2="114.1" y2="880.5"/>
          <line x1="149.4" y1="856.5" x2="149.4" y2="880.5"/><line x1="184.7" y1="856.5" x2="184.7" y2="880.5"/>
          <line x1="220" y1="856.5" x2="220" y2="880.5"/><line x1="255.3" y1="856.5" x2="255.3" y2="880.5"/>
          <line x1="291" y1="856.5" x2="291" y2="880.5"/>
        </g>
      </g>
    </svg>
  </section>

</main>
</body>
</html>
```